I want to revise my business card design and get a more modern and up to date design.

Brolvane Handyman Sevices originated from a family-owned and operated contractor business, performing home renovation, addition, and construction work in the NYC area since 2004. Today, we specialize in reliable and affordable handyman services for residential and commercial clients In 2014, we expanded to northern New Jersey. In 2016, we brought quality home improvement and repair services to new Bucks County, PA, and nearby New Jersey areas.
Target Market(s)
Home owners and business that might be looking for a General contractor, handyman, cleaning services and Home maintenance and property.
Industry/Entity Type
Construction Company
Contact Information for Business Card
I am open to new ideas
Colors
Designer to choose colors to be used in the design.
Look and feel
Each slider illustrates characteristics of the customer's brand and the style your logo design should communicate.

```html
<!DOCTYPE html>
<html lang="en">
<head>
<meta charset="utf-8">
<title>Brolvane Handyman Sevices – Business Card</title>
<link rel="stylesheet" href="https://fonts.googleapis.com/css2?family=Roboto:wght@400;500;700;900&display=swap">
<style>
  :root {
    --bg: #c8c8c8;
    --card: #ffffff;
    --brand-red: #ed1c24;
    --ink: #111111;
    --muted: #333333;
    --white: #ffffff;
  }
  * { margin: 0; padding: 0; box-sizing: border-box; }
  html, body {
    width: 1200px; height: 1200px; overflow: hidden;
    background: var(--bg);
    font-family: "Roboto", Arial, sans-serif;
  }
  .card {
    position: absolute; left: 218px; width: 800px; height: 456px;
  }
  .card--front { top: 116px; background: var(--card); }
  .card--back { top: 638px; background: var(--brand-red); }

  .brand-lockup {
    position: absolute; top: 150px; right: 56px;
    display: flex; align-items: center; gap: 14px;
  }
  .brand-lockup__mark {
    width: 70px; height: 70px; background: var(--brand-red);
  }
  .brand-lockup__text { display: flex; flex-direction: column; align-items: flex-end; }
  .brand-lockup__name {
    font-weight: 900; font-size: 58px; line-height: 1; color: var(--ink);
    letter-spacing: -1px;
  }
  .brand-lockup__tag {
    font-size: 12px; letter-spacing: 3px; color: var(--muted); margin-top: 6px;
  }
  .card--front .brand-lockup { top: 30px; }

  .contact-name {
    position: absolute; left: 59px; top: 340px;
    font-weight: 700; font-size: 28px; color: var(--brand-red); letter-spacing: 0.3px;
  }
  .contact-band {
    position: absolute; left: 0; top: 382px; width: 100%; height: 43px;
    background: var(--brand-red); color: var(--white);
    font-size: 19px; display: flex; align-items: center; padding-left: 59px;
  }
  .contact-band b { font-weight: 700; margin-right: 5px; }
  .contact-band span { margin-right: 6px; }

  .back-brand {
    position: absolute; right: 62px; top: 58px; text-align: right; color: var(--white);
  }
  .back-brand__name { font-weight: 900; font-size: 84px; line-height: 1; letter-spacing: -1px; }
  .back-brand__tag { font-size: 17px; letter-spacing: 4.5px; margin-top: 12px; font-weight: 500; }

  .services {
    position: absolute; right: 44px; top: 300px; text-align: right;
    color: var(--white); font-size: 19px; line-height: 25.5px; letter-spacing: 3px;
  }
</style>
</head>
<body>
  <section class="card card--front">
    <div class="brand-lockup">
      <div class="brand-lockup__mark"></div>
      <div class="brand-lockup__text">
        <div class="brand-lockup__name">Brolvane</div>
        <div class="brand-lockup__tag">HANDYMAN SERVICES</div>
      </div>
    </div>
    <div class="contact-name">MARCO TESSARO</div>
    <div class="contact-band">
      <b>P:</b><span>(215) 555-0187</span>
      <b>E:</b><span>brolvanehandyman@mail.com</span>
    </div>
  </section>

  <section class="card card--back">
    <div class="back-brand">
      <div class="back-brand__name">Brolvane</div>
      <div class="back-brand__tag">HANDYMAN SERVICES</div>
    </div>
    <div class="services">
      <div>Commercial and</div>
      <div>Residential Contractor</div>
      <div>Handyman, Technician Repair</div>
      <div>Improve.Maintain.Remodel</div>
    </div>
  </section>
</body>
</html>
```